Business Card Design for Photographer

Updating business card design. Must use included logo. We're a luxury wedding photography business. Elegancy, luxury, consistency are messages we wish to convey.

Visit our website at www.colbyvarnway.com to familiarize yourself more with our brand design currently (fonts, colors etc.). This is what we want to maintain.

Target Market(s)

Luxury Brides and Grooms

Industry/Entity Type

Wedding

Contact Information for Business Card

Current logo (attached to brief)
Name: Colby Varnway
Phone: 5208813047
website/blog
Email

Requirements
Must have
• Current logo (attached to brief)
• Name: Colby Varnway
• Phone: 5208813047
• website/blog
• Email
• Instagram username
Should not have
• bright colors, fonts that don't suit our brand (visit www.colbyvarnway.com)

```html
<!DOCTYPE html>
<html lang="en">
<head>
<meta charset="utf-8">
<title>Colby Varnway Photographer – Business Card</title>
<link rel="stylesheet" href="https://fonts.googleapis.com/css2?family=EB+Garamond:ital,wght@0,400;1,400&display=swap">
<style>
  :root {
    --backdrop: #d6b13d;
    --card-light: #d5d5d5;
    --card-mid: #b3b3b3;
    --ink-soft: #757575;
    --ink-deep: #6b6b6b;
    --shadow: rgba(80, 60, 10, 0.28);
  }
  * { margin: 0; padding: 0; box-sizing: border-box; }
  html, body {
    width: 1200px;
    height: 675px;
    overflow: hidden;
    background: var(--backdrop);
  }
  .canvas {
    position: relative;
    width: 1200px;
    height: 675px;
    display: flex;
    align-items: center;
    justify-content: center;
    gap: 60px;
  }
  .card {
    position: relative;
    width: 500px;
    height: 286px;
    box-shadow: 0 6px 14px var(--shadow);
  }

  /* Contact side */
  .card--contact {
    background: var(--card-light);
    color: var(--ink-soft);
    font-family: "EB Garamond", serif;
  }
  .contact-list {
    list-style: none;
    position: absolute;
    left: 58px;
    top: 64px;
  }
  .contact-item {
    display: flex;
    align-items: center;
    height: 30px;
    font-style: italic;
    font-size: 17px;
  }
  .contact-icon {
    width: 20px;
    height: 20px;
    margin-right: 12px;
    fill: var(--ink-soft);
    flex-shrink: 0;
  }
  .signature {
    position: absolute;
    right: 56px;
    bottom: 34px;
    text-align: center;
    font-style: italic;
  }
  .signature__name {
    font-size: 31px;
    line-height: 1;
  }
  .signature__role {
    font-size: 23px;
    line-height: 1.05;
  }

  /* Brand side */
  .card--brand {
    background: var(--card-mid);
    color: var(--ink-deep);
    font-family: "EB Garamond", serif;
    display: flex;
    flex-direction: column;
    align-items: center;
    justify-content: center;
  }
  .brand-mark {
    width: 66px;
    height: 66px;
    background: var(--ink-deep);
    margin-bottom: 26px;
  }
  .brand-name {
    font-size: 33px;
    letter-spacing: 0.2em;
    text-transform: uppercase;
    line-height: 1.1;
    margin-left: 0.2em;
  }
  .brand-tagline {
    font-size: 15px;
    letter-spacing: 0.48em;
    text-transform: uppercase;
    margin-top: 8px;
    margin-left: 0.48em;
  }
</style>
</head>
<body>
<main class="canvas">
  <section class="card card--contact" aria-label="Business card, contact side">
    <ul class="contact-list">
      <li class="contact-item">
        <svg class="contact-icon" viewBox="0 0 20 20" aria-hidden="true">
          <path d="M6 1h8a1.5 1.5 0 0 1 1.5 1.5v15A1.5 1.5 0 0 1 14 19H6a1.5 1.5 0 0 1-1.5-1.5v-15A1.5 1.5 0 0 1 6 1zm0 2v12h8V3zm4 13.2a1 1 0 1 0 0 2 1 1 0 0 0 0-2z"/>
        </svg>
        5208813047
      </li>
      <li class="contact-item">
        <svg class="contact-icon" viewBox="0 0 20 20" aria-hidden="true">
          <path d="M10 1a9 9 0 1 0 0 18A9 9 0 0 0 10 1zm0 1.6c1.2 1.3 2 3.2 2.2 5.6H7.8C8 5.8 8.8 3.9 10 2.6zM7.8 9.8h4.4c-.2 2.4-1 4.3-2.2 5.6-1.2-1.3-2-3.2-2.2-5.6zM6.2 8.2H2.7a7.4 7.4 0 0 1 4.9-5.3c-.8 1.4-1.3 3.2-1.4 5.3zm0 1.6c.1 2.1.6 3.9 1.4 5.3a7.4 7.4 0 0 1-4.9-5.3zm7.6 0h3.5a7.4 7.4 0 0 1-4.9 5.3c.8-1.4 1.3-3.2 1.4-5.3zm0-1.6c-.1-2.1-.6-3.9-1.4-5.3a7.4 7.4 0 0 1 4.9 5.3z"/>
        </svg>
        www.colbyvarnway.com
      </li>
      <li class="contact-item">
        <svg class="contact-icon" viewBox="0 0 20 20" aria-hidden="true">
          <path d="M1 4h18v12H1zm1.8 1.4v.3L10 10.6l7.2-4.9v-.3zm0 2V14.6h14.4V7.4L10 12.3z"/>
        </svg>
        studio@varnwaymail.com
      </li>
      <li class="contact-item">
        <svg class="contact-icon" viewBox="0 0 20 20" aria-hidden="true">
          <circle cx="10" cy="10" r="8"/>
        </svg>
        colbyvarnwayphoto
      </li>
    </ul>
    <div class="signature">
      <p class="signature__name">Colby Varnway</p>
      <p class="signature__role">Photographer</p>
    </div>
  </section>

  <section class="card card--brand" aria-label="Business card, brand side">
    <div class="brand-mark" aria-hidden="true"></div>
    <p class="brand-name">Colby Varnway</p>
    <p class="brand-tagline">Photographers</p>
  </section>
</main>
</body>
</html>
```